Design for an iOS and Android app managing shopping list

The app allows you to keep manage shopping lists, each shopping list being made of items to buy...
We need a design for the 3 screens of the app:
a) global view showing list of (shopping) list
b) form enabling to edit the name of a (shopping) list
c) detailed view listing the contents/items of a (shopping) list
d) 1 text page [not illustrated]
2 "alerts" items are also to be designed: confirm and error pop ups.
No specific guidelines, nor logo or whatever.
It will be a free app distributed on iOS and Androïd.
We just want to make it looking nice & very usable for end users.

```html
<!DOCTYPE html>
<html lang="fr">
<head>
<meta charset="utf-8">
<title>Shopping lists – app screens</title>
<link rel="stylesheet" href="https://fonts.googleapis.com/css2?family=Hind:wght@400;500;600&display=swap">
<style>
:root{
  --stage:#0d2830;
  --brand:#0a4fa3;
  --surface:#c6d5ee;
  --row:#ffffff;
  --ink:#1b1b1b;
  --green:#0f9d4a;
  --blue:#1a55a7;
  --red:#e5262b;
  --tick:#16a34a;
  --scrim:rgba(20,24,30,.55);
  --btn-grey:#e1e1e1;
}
*{box-sizing:border-box;margin:0;padding:0}
html,body{width:1200px;height:426px;overflow:hidden}
body{background:var(--stage);font-family:"Hind",sans-serif;color:var(--ink);position:relative}
.screen{position:absolute;top:24px;width:209px;height:371px;background:var(--surface);overflow:hidden}
.statusbar{height:17px;background:var(--brand);color:#fff;font-size:7.5px;display:flex;align-items:center;justify-content:space-between;padding:0 5px;position:relative}
.statusbar .time{position:absolute;left:0;right:0;text-align:center;font-weight:500}
.statusbar .battery{display:flex;align-items:center;gap:3px}
.navbar{height:29px;background:var(--brand);color:#fff;display:flex;align-items:center;justify-content:center;position:relative;font-weight:600;font-size:11px}
.navbar .left,.navbar .right{position:absolute;top:7px;width:14px;height:14px}
.navbar .left{left:8px}.navbar .right{right:9px}
.actions{display:flex;gap:11px;padding:13px 7px 0}
.btn{height:22px;border-radius:1px;color:#fff;font-size:10px;font-weight:500;display:flex;align-items:center;justify-content:center;gap:5px}
.btn svg{width:11px;height:11px}
.btn-add{background:var(--green);width:92px}
.btn-edit{background:var(--blue);width:92px;gap:18px}
.list{list-style:none;padding:12px 7px 0}
.list li{height:22px;background:var(--row);border-radius:2px;margin-bottom:2.6px;font-size:9.5px;font-weight:500;display:flex;align-items:center;justify-content:space-between;padding:0 8px 0 5px}
.list li svg{width:10px;height:10px}
.items{list-style:none;padding:12px 7px 0}
.items li{display:flex;gap:3px;margin-bottom:2.6px;height:22px}
.items .check{width:23px;background:var(--row);border-radius:2px;display:flex;align-items:center;justify-content:center}
.items .check svg{width:15px;height:15px}
.items .name{flex:1;background:var(--row);border-radius:2px;display:flex;align-items:center;justify-content:space-between;padding:0 8px 0 5px;font-size:9.5px;font-weight:500}
.items .name svg{width:9px;height:9px}
.field{margin:16px 7px 0;height:26px;background:#fff;border-radius:2px;font-size:11px;font-weight:500;padding:0 6px;display:flex;align-items:center}
.form-actions{display:flex;justify-content:space-between;padding:23px 24px 0}
.btn-save{background:var(--green);width:63px}
.btn-cancel{background:var(--red);width:63px}
.scrim{position:absolute;inset:0;background:var(--scrim)}
.dialog{position:absolute;left:7px;width:195px;height:85px;background:#fff;border-radius:2px;padding:6px 7px 8px;display:flex;flex-direction:column}
.dialog h2{font-size:12.5px;font-weight:600;text-align:center;line-height:15px}
.dialog p{font-size:9px;line-height:11px;margin-top:3px}
.dialog .buttons{display:flex;justify-content:space-between;margin-top:auto}
.dialog .buttons.end{justify-content:flex-end}
.dbtn{background:var(--btn-grey);font-size:10px;font-weight:500;padding:0 6px;height:19px;display:flex;align-items:center;border-radius:2px}
.field.muted{background:#d9d9d9}
</style>
</head>
<body>

<svg width="0" height="0" style="position:absolute">
  <defs>
    <symbol id="i-plus" viewBox="0 0 14 14"><path d="M7 1v12M1 7h12" stroke="currentColor" stroke-width="2"/></symbol>
    <symbol id="i-menu" viewBox="0 0 14 14"><path d="M1 3h12M1 7h12M1 11h12" stroke="currentColor" stroke-width="1.6"/></symbol>
    <symbol id="i-back" viewBox="0 0 14 14"><path d="M13 7H2M7 2L2 7l5 5" stroke="currentColor" stroke-width="1.6" fill="none"/></symbol>
    <symbol id="i-next" viewBox="0 0 14 14"><path d="M1 7h11M7 2l5 5-5 5" stroke="currentColor" stroke-width="1.6" fill="none"/></symbol>
    <symbol id="i-tick" viewBox="0 0 16 16"><path d="M2 8.5l4 4 8-9" stroke="var(--tick)" stroke-width="2.4" fill="none"/></symbol>
    <symbol id="i-close" viewBox="0 0 10 10"><path d="M1 1l8 8M9 1L1 9" stroke="currentColor" stroke-width="1.6"/></symbol>
    <symbol id="i-pen" viewBox="0 0 12 12"><path d="M2 10l1-3 5-5 2 2-5 5z" fill="currentColor"/></symbol>
    <symbol id="i-ok" viewBox="0 0 12 12"><path d="M1.5 6.5l3 3 6-7" stroke="currentColor" stroke-width="2" fill="none"/></symbol>
    <symbol id="i-x" viewBox="0 0 12 12"><path d="M2 2l8 8M10 2l-8 8" stroke="currentColor" stroke-width="1.8"/></symbol>
  </defs>
</svg>

<!-- Screen: all lists -->
<section class="screen" style="left:25px">
  <div class="statusbar"><span>●●●○○ KELVO</span><span class="time">4:21 PM</span><span class="battery">22% <svg width="12" height="6"><rect x=".5" y=".5" width="10" height="5" fill="none" stroke="#fff"/><rect x="1.5" y="1.5" width="2" height="3" fill="#fff"/></svg></span></div>
  <header class="navbar"><svg class="left"><use href="#i-menu"/></svg>My Lists<svg class="right"><use href="#i-plus"/></svg></header>
  <div class="actions">
    <div class="btn btn-add"><svg><use href="#i-plus"/></svg>Add new list</div>
    <div class="btn btn-edit"><svg><use href="#i-pen"/></svg>Edit</div>
  </div>
  <ul class="list">
    <li>Diner de ce soir<svg><use href="#i-next"/></svg></li>
    <li>Course Noel<svg><use href="#i-next"/></svg></li>
    <li>Courses KOMO<svg><use href="#i-next"/></svg></li>
    <li>Marché Vert<svg><use href="#i-next"/></svg></li>
    <li>Diner de ce soir<svg><use href="#i-next"/></svg></li>
    <li>Course Noel<svg><use href="#i-next"/></svg></li>
    <li>Courses KOMO<svg><use href="#i-next"/></svg></li>
    <li>Marché Vert<svg><use href="#i-next"/></svg></li>
  </ul>
</section>

<!-- Screen: list detail -->
<section class="screen" style="left:260px">
  <div class="statusbar"><span>●●●○○ KELVO</span><span class="time">4:21 PM</span><span class="battery">22% <svg width="12" height="6"><rect x=".5" y=".5" width="10" height="5" fill="none" stroke="#fff"/><rect x="1.5" y="1.5" width="2" height="3" fill="#fff"/></svg></span></div>
  <header class="navbar"><svg class="left"><use href="#i-back"/></svg>My List<svg class="right"><use href="#i-plus"/></svg></header>
  <div class="actions">
    <div class="btn btn-add"><svg><use href="#i-plus"/></svg>Add new item</div>
  </div>
  <ul class="items">
    <li><span class="check"><svg><use href="#i-tick"/></svg></span><span class="name">serviettes<svg><use href="#i-close"/></svg></span></li>
    <li><span class="check"><svg><use href="#i-tick"/></svg></span><span class="name">oignons<svg><use href="#i-close"/></svg></span></li>
    <li><span class="check"></span><span class="name">bougies<svg><use href="#i-close"/></svg></span></li>
    <li><span class="check"></span><span class="name">airelles<svg><use href="#i-close"/></svg></span></li>
    <li><span class="check"><svg><use href="#i-tick"/></svg></span><span class="name">foie gras<svg><use href="#i-close"/></svg></span></li>
    <li><span class="check"></span><span class="name">saumon fume<svg><use href="#i-close"/></svg></span></li>
    <li><span class="check"><svg><use href="#i-tick"/></svg></span><span class="name">huile d'olive<svg><use href="#i-close"/></svg></span></li>
    <li><span class="check"><svg><use href="#i-tick"/></svg></span><span class="name">Marché Vert<svg><use href="#i-close"/></svg></span></li>
  </ul>
</section>

<!-- Screen: rename with warning -->
<section class="screen" style="left:496px">
  <div class="statusbar"><span>●●●○○ KELVO</span><span class="time">4:21 PM</span><span class="battery">22% <svg width="12" height="6"><rect x=".5" y=".5" width="10" height="5" fill="none" stroke="#fff"/><rect x="1.5" y="1.5" width="2" height="3" fill="#fff"/></svg></span></div>
  <header class="navbar"><svg class="left"><use href="#i-back"/></svg>Update list name</header>
  <div class="field muted">Diner de ce soir</div>
  <div class="form-actions">
    <div class="btn btn-save"><svg><use href="#i-ok"/></svg>Save</div>
    <div class="btn btn-cancel"><svg><use href="#i-x"/></svg>Cancel</div>
  </div>
  <div class="scrim"></div>
  <div class="dialog" style="top:125px">
    <h2>Warning</h2>
    <p>List name should have atleast 1 character to be valid</p>
    <div class="buttons end"><span class="dbtn">OK</span></div>
  </div>
</section>

<!-- Screen: remove confirmation -->
<section class="screen" style="left:731px">
  <div class="statusbar"><span>●●●○○ KELVO</span><span class="time">4:21 PM</span><span class="battery">22% <svg width="12" height="6"><rect x=".5" y=".5" width="10" height="5" fill="none" stroke="#fff"/><rect x="1.5" y="1.5" width="2" height="3" fill="#fff"/></svg></span></div>
  <header class="navbar"><svg class="left"><use href="#i-menu"/></svg>My Lists<svg class="right"><use href="#i-plus"/></svg></header>
  <div class="actions">
    <div class="btn btn-add"><svg><use href="#i-plus"/></svg>Add new list</div>
    <div class="btn btn-edit"><svg><use href="#i-pen"/></svg>Edit</div>
  </div>
  <ul class="list">
    <li>Diner de ce soir<svg><use href="#i-next"/></svg></li>
    <li>Course Noel<svg><use href="#i-next"/></svg></li>
    <li>Courses KOMO<svg><use href="#i-next"/></svg></li>
    <li>Marché Vert<svg><use href="#i-next"/></svg></li>
    <li>Diner de ce soir<svg><use href="#i-next"/></svg></li>
    <li>Course Noel<svg><use href="#i-next"/></svg></li>
    <li>Courses KOMO<svg><use href="#i-next"/></svg></li>
    <li>Marché Vert<svg><use href="#i-next"/></svg></li>
  </ul>
  <div class="scrim"></div>
  <div class="dialog" style="top:100px">
    <h2>Remove shopping list</h2>
    <p>Would you like to delete the shopping list:<br>“Diner de ce soir”?</p>
    <div class="buttons"><span class="dbtn">CANCEL</span><span class="dbtn">CONFIRM</span></div>
  </div>
</section>

<!-- Screen: rename form -->
<section class="screen" style="left:966px">
  <div class="statusbar"><span>●●●○○ KELVO</span><span class="time">4:21 PM</span><span class="battery">22% <svg width="12" height="6"><rect x=".5" y=".5" width="10" height="5" fill="none" stroke="#fff"/><rect x="1.5" y="1.5" width="2" height="3" fill="#fff"/></svg></span></div>
  <header class="navbar"><svg class="left"><use href="#i-back"/></svg>Update list name</header>
  <div class="field">Diner de ce soir</div>
  <div class="form-actions">
    <div class="btn btn-save"><svg><use href="#i-ok"/></svg>Save</div>
    <div class="btn btn-cancel"><svg><use href="#i-x"/></svg>Cancel</div>
  </div>
</section>

</body>
</html>
```